I want a business card that is going to show a creative spark but without limiting me to an industry. Something edgy but that wont go out of date. I want it state My business name Serafina Loire, profession - Professional Makeup Artist contact number and email

My service is to provide makeup services from bridal, fashion, photography, film, TV and so on. It is creative and different so i want that to be reflected.

I would like the card double sided.
Updates

 I would LOVE a background on my card something like this image... i can supply an image to be formed like this

Please use the image uploaded

Can we try using the image provided on one side of the card and then writing and details on the other side

Target Market(s)

I am targeting a wide range of people from Creative directors to the individual eg. bride

Industry/Entity Type

Business

Requirements
Must have
• Name: Delphine Hartwell
contact numbe 0417853120
email address:info@serafinaloire.com
website: www.serafinaloire.com
One of the images attached

professional makeup artist / hair stylist

I want it to show creativity
Nice to have
• logo, Double-sided card
Should not have
• the design should not use tradional style. Or images that are not my own

```html
<!DOCTYPE html>
<html lang="en">
<head>
<meta charset="utf-8">
<title>Serafina Loire – Business Card</title>
<link rel="stylesheet" href="https://fonts.googleapis.com/css2?family=Lobster+Two:ital,wght@1,700&family=Goudy+Bookletter+1911&family=Advent+Pro:wght@400&display=swap">
<style>
  :root {
    --stage: #000000;
    --brand-pink: #d4157f;
    --ink: #1a1a1a;
    --label: #ffffff;
    --skin: #eab1ab;
    --skin-deep: #d98e8c;
    --lid-pink: #b8407f;
    --lid-plum: #5f4868;
    --backdrop: #cdd1c4;
    --mono-light: #e4e4e4;
    --mono-mid: #a6a6a6;
    --mono-dark: #4a4a4a;
    --soft-a: #e6e6e6;
    --soft-b: #f4f4f4;
    --soft-c: #ffffff;
  }
  * { box-sizing: border-box; margin: 0; padding: 0; }
  html, body {
    width: 1200px; height: 900px; overflow: hidden;
    background: var(--stage);
  }
  .presentation { position: relative; width: 1200px; height: 900px; }

  .card {
    position: absolute;
    width: 525px; height: 298px;
    border-radius: 72px 0 72px 0;
    overflow: hidden;
  }
  .card--front-color { left: 60px; top: 82px; }
  .card--front-mono { left: 614px; top: 82px; }
  .card--back { left: 337px; top: 461px; }

  .card__photo { position: absolute; inset: 0; }
  .card--front-color .card__photo {
    background: linear-gradient(100deg,
      var(--skin-deep) 0%, var(--skin) 12%, var(--lid-pink) 30%,
      var(--lid-plum) 44%, #b98f9c 58%, var(--backdrop) 74%,
      #dfd9cf 88%, var(--skin) 100%);
  }
  .card--front-mono .card__photo {
    background: linear-gradient(100deg,
      #bdbdbd 0%, var(--mono-light) 12%, var(--mono-mid) 30%,
      var(--mono-dark) 44%, #9c9c9c 58%, var(--mono-light) 74%,
      #d6d6d6 88%, #ececec 100%);
  }
  .card--back .card__photo {
    background: linear-gradient(100deg,
      var(--soft-a) 0%, #dcdcdc 30%, var(--soft-b) 55%, var(--soft-c) 100%);
  }

  .card__name {
    position: absolute;
    font-family: "Lobster Two", cursive;
    font-style: italic; font-weight: 700;
    color: var(--brand-pink);
    line-height: 1; white-space: nowrap;
  }
  .card__role {
    position: absolute;
    font-family: "Goudy Bookletter 1911", serif;
    font-weight: 400;
    color: var(--ink);
    line-height: 1; white-space: nowrap;
  }
  .card--front-color .card__name { left: 238px; top: 12px; font-size: 38px; }
  .card--front-color .card__role { left: 238px; top: 51px; font-size: 16px; }
  .card--front-mono .card__name { left: 238px; top: 17px; font-size: 38px; }
  .card--front-mono .card__role { left: 238px; top: 55px; font-size: 16px; }
  .card--back .card__name { left: 46px; top: 22px; font-size: 26px; }
  .card--back .card__role { left: 46px; top: 49px; font-size: 11.5px; }

  .contact {
    position: absolute; left: 237px; top: 204px;
    font-family: "Goudy Bookletter 1911", serif; font-size: 13.5px;
    list-style: none;
  }
  .contact__row { display: flex; height: 25px; align-items: center; }
  .contact__label { width: 43px; color: var(--brand-pink); }
  .contact__colon { width: 11px; color: var(--brand-pink); }
  .contact__value { color: var(--ink); }

  .side-label {
    position: absolute; width: 200px; text-align: center;
    font-family: "Advent Pro", sans-serif; font-size: 23px;
    color: var(--label);
  }
  .side-label--front { left: 498px; top: 405px; }
  .side-label--back { left: 497px; top: 784px; }
</style>
</head>
<body>
<main class="presentation">
  <section class="card card--front-color">
    <div class="card__photo" role="img" aria-label="Close-up photo of a closed eye with pink and purple shadow being applied with a brush"></div>
    <h1 class="card__name">Serafina Loire</h1>
    <p class="card__role">Professional Makeup Artist</p>
  </section>

  <section class="card card--front-mono">
    <div class="card__photo" role="img" aria-label="Black and white close-up photo of a closed eye with shadow being applied with a brush"></div>
    <h2 class="card__name">Serafina Loire</h2>
    <p class="card__role">Professional Makeup Artist</p>
  </section>

  <p class="side-label side-label--front">Front</p>

  <section class="card card--back">
    <div class="card__photo" role="img" aria-label="Faded light grey photo of a closed eye and makeup brush"></div>
    <h2 class="card__name">Serafina Loire</h2>
    <p class="card__role">Professional Makeup Artist</p>
    <ul class="contact">
      <li class="contact__row"><span class="contact__label">Tel</span><span class="contact__colon">:</span><span class="contact__value">0417 853 120</span></li>
      <li class="contact__row"><span class="contact__label">Email</span><span class="contact__colon">:</span><span class="contact__value">info@serafinaloire.com</span></li>
    </ul>
  </section>

  <p class="side-label side-label--back">Back</p>
</main>
</body>
</html>
```